Solo Law Practice Website Design

I am starting a solo law practice that will specialize in criminal defense and family law.

I have a rudimentary understanding of Wordpress as used through the hostmerry web services. The winning design would be compatible with this system so that I can modify content on my own.

I have supplied the written content and the components that I am looking for at the domain name: dorianvaskelaw.example.

I would like to take that content and work it into a website that looks more professional and inviting. The two most important goals of the website are ease of navigation and rich content for search engine spiders (for example, integrating articles into pages rather than linking to a word document).

The winning design should be turnkey for me to upload immediately.
Updates

Reason: I will be traveling.

Target Market(s)

Individuals looking for legal services.

Industry/Entity Type

Defense

Requirements
Must have
• My picture should appear at least once in the site.

The design should allow a space for me to post blog or legal updates. Additionally, there should be functionality for me to add additional articles to the site.
Nice to have
• Appropriate pictures for a legal website to break-up text on pages.

Simple flash features that won't significantly slow loading times.

Widgets that drive traffic to a contact page or function.

```html
<!DOCTYPE html>
<html lang="en">
<head>
<meta charset="utf-8">
<title>Dorian Vaske Law</title>
<link rel="stylesheet" href="https://fonts.googleapis.com/css2?family=Arimo:wght@400;700&family=Tinos:wght@400;700&display=swap">
<style>
:root{
  --page:#ebebeb;
  --ink:#1f1f1f;
  --body:#6b6b6b;
  --orange:#ee8523;
  --orange-mid:#f0992a;
  --card-text:#3b2a1e;
  --accent:#f06a1a;
  --red:#e8392e;
  --dark:#2a2a2a;
  --nav-bg:#f3f3f3;
  --footer:#d7d4d4;
  --white:#ffffff;
}
*{box-sizing:border-box;margin:0;padding:0}
html,body{width:847px;height:1200px;overflow:hidden;background:var(--page)}
body{position:relative;font-family:"Tinos",serif;color:var(--ink)}
.abs{position:absolute}
.account-bar{left:0;top:0;width:847px;height:3px;background:#8a8a8a}
.account-tab{left:600px;top:6px;width:190px;height:20px;border:1px solid #bdbdbd;border-top:none;border-radius:0 0 10px 10px;font-family:"Arimo",sans-serif;font-size:8px;color:#444;text-align:center;line-height:19px}
.account-tab a{color:var(--red);text-decoration:none}
.brand{left:78px;top:40px;font-family:"Tinos",serif;font-weight:700;font-size:34px;color:var(--ink);letter-spacing:-0.5px}
.search{left:595px;top:61px;width:189px;height:27px;background:var(--white);font-family:"Arimo",sans-serif;font-size:11px;color:#9a9a9a;line-height:27px;padding-left:12px}
.search svg{position:absolute;right:7px;top:6px}
.main-nav{left:62px;top:107px;width:717px;height:45px;display:flex;background:var(--nav-bg)}
.main-nav a{font-family:"Arimo",sans-serif;font-size:9px;letter-spacing:.6px;color:#333;text-decoration:none;display:flex;align-items:center;justify-content:center;border-right:1px solid #dcdcdc}
.main-nav a.current{background:linear-gradient(#3a3a3a,#1e1e1e);color:var(--white)}
.hero{left:62px;top:160px;width:722px;height:307px;background:radial-gradient(ellipse at 35% 40%,#4a4c4b,#262727 70%);box-shadow:0 6px 6px -4px rgba(0,0,0,.35)}
.hero-photo{left:0;top:0;width:440px;height:307px;background:linear-gradient(90deg,#2e2f2f 0%,#4a4b4b 55%,#2e2f2f 100%)}
.hero-title{left:453px;top:104px;font-size:32px;line-height:35px;color:var(--white);letter-spacing:.5px;font-weight:400}
.btn-light{background:#ededed;font-family:"Tinos",serif;font-size:12.5px;color:#333;text-align:center;line-height:27px;width:57px;height:27px}
.hero .btn-light{left:525px;top:184px}
.practice{left:62px;top:483px;width:720px;height:212px;display:flex;box-shadow:0 6px 6px -4px rgba(0,0,0,.3)}
.practice-card{position:relative;width:240px;height:100%;background:var(--orange);padding:28px 0 0 26px}
.practice-card.mid{background:var(--orange-mid)}
.practice-card h2{font-size:22px;font-weight:700;color:#3a3030;letter-spacing:.5px;line-height:26px}
.practice-card .lead{font-size:11px;margin-top:7px;color:var(--white)}
.practice-card .text{font-size:11px;line-height:15.3px;margin-top:16px;width:180px;color:var(--card-text)}
.practice-card .btn-light{position:absolute;left:27px;top:148px}
.section-title{font-size:21px;font-weight:700;color:var(--ink)}
.about-title{left:91px;top:728px}
.about-body{left:91px;top:767px;width:356px;font-size:10.8px;line-height:16.8px;color:var(--body)}
.about-body p+p{margin-top:17px}
.articles-title{left:532px;top:729px}
.article-list{left:513px;top:767px;width:250px;list-style:none}
.article-list li{position:relative;padding-left:19px;font-size:9.5px;line-height:16px;color:var(--accent);margin-bottom:16px}
.article-list li::before{content:"»";position:absolute;left:0;top:-1px;font-size:12px}
.btn-dark{background:var(--dark);color:var(--white);font-size:10px;height:21px;line-height:21px;padding:0 9px;border-radius:2px}
.read-more{left:91px;top:1027px}
.all-articles{left:532px;top:1027px}
.site-footer{left:0;top:1114px;width:847px;height:86px;background:var(--footer);text-align:center}
.footer-brand{margin-top:19px;font-size:22px;font-weight:700;color:#767272}
.copyright{margin-top:6px;font-size:8.5px;color:#5e5e5e}
</style>
</head>
<body>
<div class="abs account-bar"></div>
<div class="abs account-tab">Have an account? <a href="#">LOGIN</a> or <a href="#">SIGN-UP</a></div>

<div class="abs brand">Dorian Vaske Law</div>

<div class="abs search">Search
  <svg width="16" height="16" viewBox="0 0 16 16"><circle cx="6.5" cy="6.5" r="4.8" fill="none" stroke="#333" stroke-width="1.8"/><line x1="10" y1="10" x2="14.5" y2="14.5" stroke="#333" stroke-width="2.4" stroke-linecap="round"/></svg>
</div>

<nav class="abs main-nav">
  <a href="#" class="current" style="width:73px">HOME</a>
  <a href="#" style="width:101px">ABOUT</a>
  <a href="#" style="width:128px">SERVICES</a>
  <a href="#" style="width:119px">PRACTICE</a>
  <a href="#" style="width:93px">BLOG</a>
  <a href="#" style="width:104px">ARTICLES</a>
  <a href="#" style="width:99px;border-right:none">CONTACTS</a>
</nav>

<section class="abs hero">
  <div class="abs hero-photo" role="img" aria-label="Portrait photo of the attorney"></div>
  <h1 class="abs hero-title">NEED LEGAL<br>ASSISTANCE?</h1>
  <div class="abs btn-light">MORE</div>
</section>

<section class="abs practice">
  <div class="practice-card">
    <h2>CRIMINAL LAW</h2>
    <p class="lead">Vestibulum liberotctis et quasee.</p>
    <p class="text">Nam elit magna endrerit sit amet tincidunt ac viverra sed nullnec porta dim ssae diam lorem.</p>
    <div class="btn-light">MORE</div>
  </div>
  <div class="practice-card mid">
    <h2>FAMILY&nbsp; LAW</h2>
    <p class="lead">Vestibulum liberotctis et quasee.</p>
    <p class="text">Nam elit magna endrerit sit amet tincidunt ac viverra sed nullnec porta dim ssae diam lorem.</p>
    <div class="btn-light">MORE</div>
  </div>
  <div class="practice-card">
    <h2>DEFENCE LAW</h2>
    <p class="lead">Vestibulum liberotctis et quasee.</p>
    <p class="text">Nam elit magna endrerit sit amet tincidunt ac viverra sed nullnec porta dim ssae diam lorem.</p>
    <div class="btn-light">MORE</div>
  </div>
</section>

<h2 class="abs section-title about-title">About Dorian Vaske Law</h2>
<div class="abs about-body">
  <p>Lorem ipsum dolor sit amet, consectetur adipisicing elit, sed do eiusmod tempor incididunt ut labore et dolore magna aliqua. Ut enim ad minim veniam, quis nostrud exercitation ullamco laboris nisi ut aliquip ex ea commodo consequat. Duis aute irure dolor in rep- rehenderit in voluptate velit esse cillum dolore eu fugiat nulla pariatur. Excepteur sint occaecat cupidatat non proident, sunt in culpa qui officia deserunt mollit anim id est laborum.</p>
  <p>Ut enim ad minim veniam, quis nostrud exercitation ullamco laboris nisi ut aliquip ex ea commodo consequat. Duis aute irure dolor in rep- rehenderit in voluptate velit esse cillum dolore eu fugiat nulla pariatur. Excepteur sint occaecat cupidatat non proident, sunt in culpa qui officia deserunt mollit anim id est laborum.&nbsp;&nbsp; Enim ad minim veniam, quis nostrud exercitation ullamco laboris nisi ut aliquip ex ea commodo consequat. Duis aute irure dolor in rep- rehenderit in voluptate velit esse cillum dolore eu</p>
</div>
<div class="abs btn-dark read-more">Read more</div>

<h2 class="abs section-title articles-title">Recent Articles</h2>
<ul class="abs article-list">
  <li>Ut enim ad minim veniam, quis</li>
  <li>Duis aute irure dolor in rep- rehenderit in<br>voluptate velit esse cillum dolore</li>
  <li>Enim ad minim veniam, quis nostrud exercitation<br>ullamco laboris</li>
  <li>Duis aute irure dolor in rep- rehenderit</li>
  <li>Ut enim ad minim veniam, quis nostrud</li>
  <li>Lorem ipsum dolor sit amet, consectetur adipisicing<br>elit, sed do eiusmod</li>
</ul>
<div class="abs btn-dark all-articles">Read all articles</div>

<footer class="abs site-footer">
  <div class="footer-brand">Dorian Vaske Law</div>
  <p class="copyright">Copyright © 2012.&nbsp; All Rights Reserved</p>
</footer>
</body>
</html>
```